Boutique custom software development company needs new business card

Our nearly 20 year old custom software development company would like to better include the fact that we are now providing Bitcoin services. These new services are B2B include education (how to acquire and securely hold Bitcoin) and integrating Bitcoin payments into existing ecommerce sites or other existing systems. Please keep the card clean and simple. Attached is our current design and some other files. vexalon.example

Target Market(s)

businesses owners interested in long term relationship

Industry/Entity Type

Custom software development and Bitcoin

Contact Information for Business Card

Marcus Ellwood, marcus@vexalon.example, vexalon.example, (888) 555-VEXAL

Font styles to use
Other font styles liked:
• monospace

Requirements
Must have
• double-sided
Nice to have
• clean and simple
Should not have
• physical address

```html
<!DOCTYPE html>
<html lang="en">
<head>
<meta charset="utf-8">
<title>Vexalon Business Card</title>
<link href="https://fonts.googleapis.com/css2?family=Roboto+Mono:wght@400;500;700&family=Lato:wght@400&display=swap" rel="stylesheet">
<style>
  :root {
    --page-bg: #d3d4d6;
    --navy: #0a1737;
    --navy-tile: #15224f;
    --white: #ffffff;
    --card-light: #dce4ee;
    --brand-blue: #3c78bb;
    --brand-orange: #e0782c;
    --ink: #1c1f26;
  }
  * { margin: 0; padding: 0; box-sizing: border-box; }
  html, body { width: 900px; height: 1200px; overflow: hidden; }
  body { background: var(--page-bg); position: relative; font-family: "Roboto Mono", monospace; }

  .card { position: absolute; width: 656px; height: 374px; border-radius: 14px; overflow: hidden; }

  /* Front */
  .card--front { left: 123px; top: 191px; background: radial-gradient(ellipse at 50% 45%, #0d1c44 0%, var(--navy) 70%); }
  .front-wordmark {
    position: absolute; left: 0; right: 0; top: 150px; text-align: center;
    font-family: "Roboto Mono", monospace; font-weight: 700; font-size: 62px;
    color: var(--white); letter-spacing: -1px; line-height: 1;
  }
  .service { position: absolute; top: 289px; width: 141px; height: 67px; border-radius: 6px; background: var(--navy-tile); }
  .service__icon {
    position: absolute; left: 52px; top: -27px; width: 37px; height: 37px; border-radius: 9px;
    background: radial-gradient(circle at 40% 35%, #e8eefb 0%, #a8bce6 60%, #6a86c9 100%);
  }
  .service__label {
    position: absolute; left: 0; right: 0; top: 18px; text-align: center;
    font-weight: 500; font-size: 14px; line-height: 19px; color: var(--white); letter-spacing: 0.2px;
  }

  /* Back */
  .card--back { left: 123px; top: 622px; background: linear-gradient(135deg, #e1e8f0 0%, #d6e0eb 100%); }
  .back-wordmark {
    position: absolute; left: 27px; top: 34px;
    font-family: "Roboto Mono", monospace; font-weight: 700; font-size: 64px;
    color: var(--brand-blue); letter-spacing: -2px; line-height: 1;
  }
  .tagline {
    position: absolute; left: 38px; top: 90px;
    font-family: "Lato", sans-serif; font-size: 18px; color: var(--brand-blue); letter-spacing: -0.6px;
  }
  .brand-square { position: absolute; left: 464px; top: 35px; width: 157px; height: 157px; background: var(--brand-blue); }
  .person-name { position: absolute; left: 28px; top: 203px; font-weight: 700; font-size: 26px; color: var(--brand-blue); letter-spacing: 0.2px; }
  .person-role { position: absolute; left: 28px; top: 234px; font-size: 15px; color: var(--ink); letter-spacing: 1px; }
  .divider { position: absolute; left: 27px; top: 261px; width: 594px; height: 1.5px; background: var(--brand-orange); }
  .contact-list { position: absolute; left: 27px; top: 276px; list-style: none; }
  .contact-list li { display: flex; align-items: center; height: 29px; font-size: 15px; color: var(--ink); letter-spacing: 1.2px; }
  .contact-list svg { width: 15px; height: 15px; margin-right: 7px; flex: none; }
</style>
</head>
<body>

<section class="card card--front" aria-label="Card front">
  <div class="front-wordmark">VEXALON</div>

  <div class="service" style="left:20px">
    <div class="service__icon" role="img" aria-label="Toggle switches icon"></div>
    <p class="service__label">WEB AND NATIVE<br>APPLICATIONS</p>
  </div>
  <div class="service" style="left:178px">
    <div class="service__icon" role="img" aria-label="Robot head icon" style="border-radius:50%"></div>
    <p class="service__label">DIGITAL PROCESS<br>AUTOMATION</p>
  </div>
  <div class="service" style="left:336px">
    <div class="service__icon" role="img" aria-label="Cloud icon" style="border-radius:50%"></div>
    <p class="service__label">CLOUD-BASED<br>PORTALS</p>
  </div>
  <div class="service" style="left:494px">
    <div class="service__icon" role="img" aria-label="Brain icon" style="border-radius:50%"></div>
    <p class="service__label">BITCOIN<br>CONSULTING</p>
  </div>
</section>

<section class="card card--back" aria-label="Card back">
  <div class="back-wordmark">VEXALON</div>
  <p class="tagline">developer of custom applications</p>
  <div class="brand-square"></div>

  <h1 class="person-name">Marcus Ellwood</h1>
  <p class="person-role">Founder</p>
  <div class="divider"></div>

  <ul class="contact-list">
    <li>
      <svg viewBox="0 0 24 24" aria-hidden="true"><path fill="#e0782c" d="M6.6 10.8a15.1 15.1 0 0 0 6.6 6.6l2.2-2.2c.3-.3.7-.4 1-.2 1.1.4 2.3.6 3.6.6.6 0 1 .4 1 1V20c0 .6-.4 1-1 1A17 17 0 0 1 3 4c0-.6.4-1 1-1h3.5c.6 0 1 .4 1 1 0 1.3.2 2.5.6 3.6.1.3 0 .7-.2 1z"/></svg>
      (888) 555-VEXAL
    </li>
    <li>
      <svg viewBox="0 0 24 24" aria-hidden="true"><rect x="2" y="5" width="20" height="14" fill="#e0782c"/><path d="M2 5l10 8 10-8M2 19l7-7M22 19l-7-7" stroke="#dce4ee" stroke-width="1.6" fill="none"/></svg>
      marcus@vexalon.example
    </li>
    <li>
      <svg viewBox="0 0 24 24" aria-hidden="true" fill="none" stroke="#e0782c" stroke-width="1.8"><circle cx="12" cy="12" r="9.5"/><ellipse cx="12" cy="12" rx="4" ry="9.5"/><path d="M2.5 12h19M4 7h16M4 17h16"/></svg>
      www.vexalon.example
    </li>
  </ul>
</section>

</body>
</html>
```